Lanternfield - Afro Jazz CD Cover design project

CD Cover design for a jazz album. Starting off as a single/ep release; and then full album release a month later. So cover presentation for box set (physical print) and online distribution. Also alternate cover presentation for movement from EP to full album.
Songs on Ep:Red Kites; Lanternfield; Tin Harbor; Kolo Meti

Music is Afro Jazz. Album Title is: Lanternfield
Artist: Tobias
Producer: Tobias R
Releasing label: RV Music

Project Deadline Extended Reason: My apologies for the inconvenience to everyone. Not well enough to review all designs by today's set deadline. I hope to start doing so and providing feedback in the next few days. Thank you for your submissions. Please continue to submit. Added Wednesday, October 7, 2015

Project Deadline Extended Reason: Hi, Forgive my lack of feedback for the most part; unforseen circumstances. I have looked at some of the designs though and commented on a few. I am of the opinion there could be vast improvements and so am going to provide a 5 day extension as well as a $50 increase in the price money to hopefully inspire greater looking designs and concepts. Thank you. Added Friday, October 30, 2015

Hi guys. I am so sorry I have taken so long. I have considered the designs presented and there are some good concepts there. I must say however that I have not found one that stands out and captivates me. I am left with the choice of selecting among the short list or increasing the amount by another $30 or $50 and hoping for that elusive one, that one of you may yet come up with; what do you think.

Target Market(s)

Global; late teens to fifties; cross cultural

Font styles to use
Script

Requirements
Must have
• Cover (online); Box set (physical print)
• Alternate cover (EP and Album release)
Nice to have
• Creativity and originality. Covers that attract attention, a work of art in itself, evoking an emotional response on its own merits. Remember this is Afro Jazz, not just for Afro audience but global.

```html
<!DOCTYPE html>
<html lang="en">
<head>
<meta charset="utf-8">
<title>Tobias – Lanternfield CD Cover</title>
<link rel="stylesheet" href="https://fonts.googleapis.com/css2?family=Bungee&family=Yanone+Kaffeesatz:wght@400&family=Arimo&display=swap">
<style>
  :root {
    --bg: #ffffff;
    --ink: #2a1a12;
    --orange: #e8781f;
    --brown: #6b3a1c;
    --brown-dark: #3b1f10;
    --white: #ffffff;
    --panel-text: #1a1a1a;
    --hub: #e9e9e9;
  }
  html, body {
    margin: 0;
    padding: 0;
    width: 1200px;
    height: 645px;
    overflow: hidden;
    background: var(--bg);
  }
  .canvas { display: block; width: 1200px; height: 645px; }
  .view-label {
    font-family: "Arimo", Arial, sans-serif;
    font-size: 34px;
    fill: var(--ink);
  }
  .cover-bg { fill: var(--orange); }
  .artwork { fill: url(#artworkTone); }
  .swirl { fill: var(--brown); }
  .swirl-dark { fill: var(--brown-dark); }
  .display {
    font-family: "Bungee", Impact, sans-serif;
    fill: var(--white);
    stroke: var(--brown-dark);
    stroke-width: 1.2px;
    paint-order: stroke;
    filter: drop-shadow(3px 3px 0 rgba(40, 20, 10, 0.85));
  }
  .tracklist {
    font-family: "Yanone Kaffeesatz", "Arial Narrow", sans-serif;
    fill: var(--white);
    font-size: 30px;
  }
  .disc-tracks {
    font-family: "Yanone Kaffeesatz", "Arial Narrow", sans-serif;
    fill: var(--white);
    font-size: 18px;
  }
  .fine-print {
    font-family: "Arimo", Arial, sans-serif;
    fill: var(--white);
    font-size: 9px;
  }
  .info-box { fill: var(--white); }
  .info-text {
    font-family: "Arimo", Arial, sans-serif;
    fill: var(--panel-text);
    font-size: 11px;
  }
  .spine { fill: var(--brown-dark); }
  .spine-title {
    font-family: "Bungee", Impact, sans-serif;
    fill: var(--white);
    font-size: 12px;
    letter-spacing: 1px;
  }
  .spine-label {
    font-family: "Arimo", Arial, sans-serif;
    fill: var(--white);
    font-size: 9px;
  }
  .disc-hub { fill: var(--hub); }
  .disc-hole { fill: var(--bg); }
</style>
</head>
<body>
<svg class="canvas" viewBox="0 0 1200 645" xmlns="http://www.w3.org/2000/svg">
  <defs>
    <linearGradient id="artworkTone" x1="0" y1="0" x2="0" y2="1">
      <stop offset="0" stop-color="#f08a2c"/>
      <stop offset="1" stop-color="#c9641a"/>
    </linearGradient>
    <clipPath id="frontClip"><rect x="20" y="95" width="380" height="470"/></clipPath>
    <clipPath id="backClip"><rect x="770" y="95" width="410" height="470"/></clipPath>
    <clipPath id="discClip"><circle cx="560" cy="330" r="175"/></clipPath>
    <path id="discTop" d="M 420 330 A 140 140 0 0 1 700 330"/>
    <path id="discBottom" d="M 410 330 A 150 150 0 0 0 710 330"/>
  </defs>

  <text class="view-label" x="230" y="55" text-anchor="middle">Front</text>
  <text class="view-label" x="975" y="55" text-anchor="middle">Back</text>

  <!-- Disc -->
  <g class="disc">
    <circle class="cover-bg" cx="560" cy="330" r="175"/>
    <g clip-path="url(#discClip)">
      <path class="swirl" d="M 385 150 L 740 150 L 740 300 C 660 250 590 270 540 310 C 490 260 430 210 385 150 Z"/>
      <path class="swirl-dark" d="M 560 510 C 620 460 680 440 740 400 L 740 510 Z" opacity="0.55"/>
    </g>
    <text class="display" font-size="26"><textPath href="#discTop" startOffset="50%" text-anchor="middle">LANTERNFIELD</textPath></text>
    <text class="display" font-size="26"><textPath href="#discBottom" startOffset="78%" text-anchor="middle">TOBIAS</textPath></text>
    <text class="disc-tracks" x="470" y="385">1. Red Kites</text>
    <text class="disc-tracks" x="470" y="405">2. Lanternfield</text>
    <text class="disc-tracks" x="470" y="425">3. Tin Harbor</text>
    <text class="disc-tracks" x="470" y="445">4. Kolo Meti</text>
    <text class="fine-print" x="472" y="461">Producer: Tobias R</text>
    <text class="fine-print" x="472" y="473">Releasing label: RV Music</text>
    <circle class="disc-hub" cx="560" cy="330" r="38"/>
    <circle class="disc-hole" cx="560" cy="330" r="16"/>
  </g>

  <!-- Front cover -->
  <g class="front-cover" clip-path="url(#frontClip)">
    <rect class="cover-bg" x="20" y="95" width="380" height="470"/>
    <rect class="artwork" x="20" y="95" width="180" height="360" role="img" aria-label="Tribal mask illustration with sun, triangle and arrow motifs in dark brown on orange"/>
    <path class="swirl" d="M 210 95 L 400 95 L 400 350 C 340 320 280 310 250 270 C 215 220 208 160 210 95 Z"/>
    <path class="swirl-dark" d="M 90 390 C 170 320 280 330 340 390 C 280 370 200 375 140 430 Z"/>
    <path class="swirl" d="M 20 500 C 80 410 190 370 290 410 C 210 420 140 470 110 565 L 20 565 Z"/>
    <text class="display" x="40" y="525" font-size="44">TOBIAS</text>
    <text class="display" font-size="34" transform="translate(392 548) rotate(-90)">LANTERNFIELD</text>
  </g>

  <!-- Spine -->
  <rect class="spine" x="740" y="95" width="30" height="470"/>
  <text class="spine-label" transform="translate(759 110) rotate(90)">RV Music</text>
  <text class="spine-title" transform="translate(760 200) rotate(90)">TOBIAS   LANTERNFIELD</text>

  <!-- Back cover -->
  <g class="back-cover" clip-path="url(#backClip)">
    <rect class="cover-bg" x="770" y="95" width="410" height="470"/>
    <rect class="artwork" x="770" y="95" width="200" height="290" role="img" aria-label="Tribal mask illustration with sun, triangle and arrow motifs in dark brown on orange"/>
    <path class="swirl" d="M 965 115 C 1065 85 1180 125 1180 215 L 1180 565 L 1095 565 C 1085 455 1005 355 965 265 C 945 210 940 150 965 115 Z"/>
    <path class="swirl" d="M 770 320 C 845 290 935 320 985 360 C 905 380 835 450 805 565 L 770 565 Z" opacity="0.9"/>
    <text class="display" x="975" y="215" font-size="30">TOBIAS</text>
    <text class="display" font-size="28" transform="translate(1172 545) rotate(-90)">LANTERNFIELD</text>
    <text class="tracklist" x="880" y="360">1. Red Kites</text>
    <text class="tracklist" x="880" y="392">2. Lanternfield</text>
    <text class="tracklist" x="880" y="424">3. Tin Harbor</text>
    <text class="tracklist" x="880" y="456">4. Kolo Meti</text>
    <rect class="info-box" x="780" y="478" width="300" height="66" rx="2"/>
    <text class="info-text" x="787" y="494">Music is Afro Jazz. Album Title is: Lanternfield</text>
    <text class="info-text" x="787" y="508">Artist: Tobias</text>
    <text class="info-text" x="787" y="522">Producer: Tobias R</text>
    <text class="info-text" x="787" y="536">Releasing label: RV Music</text>
  </g>
</svg>
</body>
</html>
```